Einladungskarten-Design für Ehepaar
Zielgruppe
Wir sind ein Ehepaar und feiern 2 Geburtstage und eine Hochzeit in einem grossen Fest. Unsere Zielgruppe sind unsere Freunde.
Aufgabenstellung
Doppelkarte A5 quer, nur Frontseite designed; Briefing siehe Worddok

```html
<!DOCTYPE html>
<html lang="de">
<head>
<meta charset="utf-8">
<title>Einladung – Doppelter Geburtstag und Hochzeit</title>
<link rel="stylesheet" href="https://fonts.googleapis.com/css2?family=Archivo:wght@700&family=Open+Sans:wght@300;400;600&family=Work+Sans:wght@300;400&display=swap">
<style>
  :root {
    --leaf-dark: #347a4a;
    --leaf-mid: #5c9a6c;
    --paper: #ffffff;
    --green-bright: #1faa4a;
    --green-deep: #1e6b3c;
    --circle: #6ab153;
    --pink: #ff1aa0;
  }
  html, body {
    margin: 0;
    padding: 0;
    width: 1200px;
    height: 810px;
    overflow: hidden;
    background: var(--paper);
  }
  .card {
    position: relative;
    width: 1200px;
    height: 810px;
    overflow: hidden;
    background: var(--paper);
  }
  .jungle-photo {
    position: absolute;
    inset: 0;
    background:
      radial-gradient(ellipse 260px 220px at 330px 420px, rgba(255,255,255,0.95), rgba(255,255,255,0) 70%),
      linear-gradient(160deg, var(--leaf-mid) 0%, var(--leaf-dark) 45%, #2f7045 100%);
  }
  .headline {
    position: absolute;
    left: 192px;
    top: 72px;
    margin: 0;
    font-family: 'Work Sans', sans-serif;
    font-weight: 400;
    font-size: 70px;
    letter-spacing: 0.5px;
    line-height: 1;
    color: var(--green-deep);
    white-space: nowrap;
  }
  .headline .accent { color: var(--green-bright); }
  .occasion-box {
    position: absolute;
    left: 70px;
    top: 141px;
    width: 466px;
    height: 138px;
    background: var(--paper);
  }
  .occasion {
    position: absolute;
    left: 68px;
    top: 135px;
    width: 470px;
    margin: 0;
    font-family: 'Archivo', sans-serif;
    font-weight: 700;
    font-size: 29px;
    line-height: 36px;
    text-align: center;
    color: var(--pink);
    white-space: nowrap;
  }
  .badge {
    position: absolute;
    border-radius: 50%;
    background: var(--circle);
    color: var(--paper);
    font-family: 'Open Sans', sans-serif;
  }
  .badge--main {
    left: 770px; top: 20px; width: 380px; height: 380px;
  }
  .badge--main .figure {
    position: absolute;
    left: 0; right: 0;
    top: 126px;
    text-align: center;
    font-family: 'Archivo', sans-serif;
    font-weight: 700;
    font-size: 122px;
    line-height: 120px;
  }
  .badge--main .detail {
    position: absolute;
    left: 0; right: 0;
    top: 279px;
    display: flex;
    justify-content: center;
    align-items: center;
    font-weight: 300;
  }
  .detail .counts {
    display: flex;
    flex-direction: column;
    font-size: 32px;
    line-height: 26px;
    margin-right: 2px;
  }
  .detail .labels {
    display: flex;
    flex-direction: column;
    font-size: 19px;
    line-height: 26px;
    font-weight: 400;
  }
  .detail .amp {
    font-size: 52px;
    margin-left: 10px;
    line-height: 1;
  }
  .badge--decades,
  .badge--date {
    display: flex;
    align-items: center;
    justify-content: center;
    font-weight: 300;
  }
  .badge--decades {
    left: 537px; top: 237px; width: 170px; height: 170px;
    font-size: 60px;
  }
  .badge--date {
    left: 441px; top: 385px; width: 86px; height: 86px;
    font-size: 27px;
  }
</style>
</head>
<body>
  <main class="card">
    <div class="jungle-photo" role="img" aria-label="Grün-weiß eingefärbtes Foto eines Dschungels mit Bananenstauden"></div>

    <h1 class="headline"><span class="accent">EIN</span>LADUNG</h1>

    <div class="occasion-box"></div>
    <p class="occasion">DREIFACH GRUND ZU FEIERN<br>DOPPELTER GEBURTSTAG<br>UND EINE HOCHZEIT<br>FEST AM 6.10.2018</p>

    <div class="badge badge--main">
      <span class="figure">60x2</span>
      <div class="detail">
        <span class="counts"><span>2</span><span>1</span></span>
        <span class="labels"><span>Geburtstage</span><span>&nbsp;Hochzeit</span></span>
        <span class="amp">&amp;</span>
      </div>
    </div>

    <div class="badge badge--decades">6x10</div>
    <div class="badge badge--date">6.10.</div>
  </main>
</body>
</html>
```